Lakemond Drywork Business Card Design

Professional and clean design. The design colors should flow with the logo. Two-sided card with the website on the back which is:

www.LakemondDrywork.example.

"Specializing in Water Damage Restoration"

On the front I need the name, email, phone, and logo.

Name: Darnell Quimby
Email: Darnell@LakemondDrywork.example
Phone: 555-018-2364 for now

I only have the Preview and Thumbnail right now but should have the source files uploaded within a day or two.

Target Market(s)

Flood victims, home owners with water damage from busted pipes etc...

Industry/Entity Type

Business

Contact Information for Business Card

Name: Darnell Quimby

Font styles to use
Serif
Sans Serif

Requirements
Must have
• Business Card Details Info

```html
<!DOCTYPE html>
<html lang="en">
<head>
<meta charset="utf-8">
<title>Lakemond Drywork Business Card</title>
<link href="https://fonts.googleapis.com/css2?family=Cinzel:wght@600&family=Lato:wght@400;700;900&display=swap" rel="stylesheet">
<style>
  :root {
    --page-bg: #e9ecef;
    --card-bg: #ffffff;
    --sky-blue: #55b5e6;
    --deep-blue: #1b79cb;
    --brand-blue: #2a86d2;
    --ink: #222a30;
    --rule-blue: #2a8fd8;
  }
  * { box-sizing: border-box; margin: 0; padding: 0; }
  html, body { width: 1200px; height: 913px; overflow: hidden; }
  body { background: var(--page-bg); position: relative; font-family: "Lato", Arial, sans-serif; }

  .card {
    position: absolute;
    width: 560px; height: 320px;
    background: var(--card-bg);
    box-shadow: 0 10px 28px rgba(0,0,0,.18);
    overflow: hidden;
  }
  .card--back { left: 60px; top: 110px; }
  .card--front { left: 580px; top: 480px; }

  .band { position: absolute; box-shadow: -6px 4px 10px rgba(0,0,0,.12); }
  .band--back-left { left: 0; top: 190px; width: 200px; height: 62px;
    background: linear-gradient(90deg, var(--deep-blue), #3a9ee0); }
  .band--back-right { right: 0; top: 66px; width: 180px; height: 62px; background: var(--sky-blue); }
  .band--front-name { right: 0; top: 40px; width: 240px; height: 64px; background: var(--sky-blue);
    display: flex; align-items: center; justify-content: center; }
  .band--front-left { left: 0; top: 176px; width: 100px; height: 52px; background: var(--deep-blue); }

  .brand { position: absolute; display: flex; align-items: center; gap: 10px; }
  .brand__dot { width: 30px; height: 30px; border-radius: 50%; background: var(--sky-blue); flex: none; }
  .brand__name { font-family: "Cinzel", Georgia, serif; font-weight: 600; font-size: 23px;
    color: var(--brand-blue); letter-spacing: 1px; white-space: nowrap; }
  .card--back .brand { left: 120px; top: 142px; }
  .card--front .brand { left: 130px; top: 124px; }

  .back-info { position: absolute; left: 210px; width: 340px; top: 202px; text-align: center;
    font-size: 14px; line-height: 1.4; color: var(--ink); }

  .holder-name { color: #fff; font-size: 18px; letter-spacing: .5px; text-transform: uppercase; white-space: nowrap; }
  .holder-name__first { font-weight: 900; }
  .holder-name__last { font-weight: 400; }

  .contact { position: absolute; left: 160px; right: 24px; top: 214px; list-style: none; font-size: 15px; color: var(--ink); }
  .contact__item { display: flex; align-items: center; gap: 10px; height: 32px; }
  .contact__item--phone { border-bottom: 1px solid var(--rule-blue); }
  .contact__icon { width: 16px; height: 16px; flex: none; }
</style>
</head>
<body>

<section class="card card--back" aria-label="Card back">
  <div class="band band--back-left"></div>
  <div class="band band--back-right"></div>
  <div class="brand">
    <span class="brand__dot"></span>
    <span class="brand__name">Lakemond Drywork</span>
  </div>
  <div class="back-info">
    <p class="tagline">Specializing in Water Damage Restoration</p>
    <p class="website">www.LakemondDrywork.example</p>
  </div>
</section>

<section class="card card--front" aria-label="Card front">
  <div class="band band--front-name">
    <p class="holder-name"><span class="holder-name__first">Darnell</span> <span class="holder-name__last">Quimby</span></p>
  </div>
  <div class="band band--front-left"></div>
  <div class="brand">
    <span class="brand__dot"></span>
    <span class="brand__name">Lakemond Drywork</span>
  </div>
  <ul class="contact">
    <li class="contact__item contact__item--phone">
      <svg class="contact__icon" viewBox="0 0 16 16" aria-hidden="true"><path fill="#222a30" d="M1 5c0-2 2-3 7-3s7 1 7 3v1h-3V4.5H4V6H1zM3 7h10l1 7H2zm5 2a2 2 0 1 0 0 4 2 2 0 0 0 0-4z"/></svg>
      <span>(555) 018-2364</span>
    </li>
    <li class="contact__item">
      <svg class="contact__icon" viewBox="0 0 16 16" aria-hidden="true"><rect x="1" y="3" width="14" height="10" fill="#222a30"/><path d="M1.5 3.5 8 9l6.5-5.5" stroke="#fff" stroke-width="1.2" fill="none"/></svg>
      <span>Darnell@LakemondDrywork.example</span>
    </li>
  </ul>
</section>

</body>
</html>
```